Wholesale in Gold Jewellery & Gold Bullion

We are an established gold jewellery and gold bullion wholesaler selling these products to international clients. We already have a name and logo of our company, hence please view attached current card design. We need a completely new design to compliment our business and industry and the final design should be new and elegant.

Contact Information for Business Card

New card details must be same as per current card. Like logo, name, tel no. & etc.

Colors

Designer to choose colors to be used in the design.

```html
<!DOCTYPE html>
<html lang="en">
<head>
<meta charset="utf-8">
<title>Kavira &amp; Co Business Card</title>
<link href="https://fonts.googleapis.com/css2?family=Mulish:wght@400;500;600&display=swap" rel="stylesheet">
<style>
  :root {
    --backdrop: #e4e4e4;
    --gold: #d99611;
    --ink: #2e2e2e;
    --paper: #ffffff;
    --shadow: rgba(0,0,0,0.18);
  }
  * { box-sizing: border-box; margin: 0; padding: 0; }
  html, body {
    width: 1200px; height: 900px; overflow: hidden;
    background: var(--backdrop);
    font-family: "Mulish", sans-serif;
  }
  .card {
    position: absolute; left: 280px; width: 640px; height: 366px;
    box-shadow: 0 8px 22px var(--shadow);
  }
  .card-front { top: 60px; background: var(--gold); }
  .card-back { top: 474px; background: var(--paper); }

  /* front */
  .front-brand {
    position: absolute; left: 50%; top: 50%;
    transform: translate(-50%, -50%);
    display: flex; align-items: center; gap: 26px;
  }
  .brand-dot {
    width: 64px; height: 64px; border-radius: 50%;
    background: var(--paper);
  }
  .wordmark { text-align: center; }
  .wordmark-name {
    font-size: 34px; font-weight: 500; letter-spacing: 1px;
    color: var(--paper); line-height: 1;
  }
  .wordmark-sub {
    display: flex; align-items: center; gap: 10px;
    margin-top: 8px; font-size: 11px; letter-spacing: 2px;
    color: var(--paper); font-weight: 500;
  }
  .wordmark-sub::before, .wordmark-sub::after {
    content: ""; flex: 1; height: 1px; background: var(--paper);
  }

  /* back */
  .back-brand {
    position: absolute; left: 40px; top: 70px;
    display: flex; align-items: center; gap: 30px;
  }
  .back-brand .brand-dot { background: var(--gold); width: 80px; height: 80px; }
  .back-brand .wordmark-name { color: var(--ink); font-size: 40px; }
  .back-brand .wordmark-sub { color: var(--gold); }
  .back-brand .wordmark-sub::before,
  .back-brand .wordmark-sub::after { background: var(--gold); }

  .person { position: absolute; left: 40px; top: 200px; }
  .person-name {
    font-size: 19px; font-weight: 500; letter-spacing: 0.5px;
    color: var(--gold); text-transform: uppercase;
  }
  .person-role { font-size: 15px; color: var(--ink); margin-top: 2px; }

  .contact-list {
    list-style: none; position: absolute; left: 40px; top: 262px;
    font-size: 15px; color: var(--ink); line-height: 1.45;
  }
  .contact-list li { display: flex; align-items: center; gap: 10px; }
  .contact-list svg { width: 14px; height: 14px; fill: var(--gold); flex: none; }

  .address {
    position: absolute; right: 40px; top: 200px;
    text-align: right; font-size: 14px; color: var(--ink); line-height: 1.35;
  }
</style>
</head>
<body>

<section class="card card-front">
  <div class="front-brand">
    <span class="brand-dot"></span>
    <div class="wordmark">
      <div class="wordmark-name">KAVIRA &amp; CO</div>
      <div class="wordmark-sub">PTE LTD</div>
    </div>
  </div>
</section>

<section class="card card-back">
  <div class="back-brand">
    <span class="brand-dot"></span>
    <div class="wordmark">
      <div class="wordmark-name">KAVIRA &amp; CO</div>
      <div class="wordmark-sub">PTE LTD</div>
    </div>
  </div>

  <div class="person">
    <div class="person-name">Ravin Sethuraman</div>
    <div class="person-role">Director</div>
  </div>

  <ul class="contact-list">
    <li>
      <svg viewBox="0 0 16 16" aria-hidden="true"><path d="M3 2h3l1.5 3.5-2 1.3a8 8 0 0 0 3.7 3.7l1.3-2L14 10v3a1 1 0 0 1-1 1A11 11 0 0 1 2 3a1 1 0 0 1 1-1z"/></svg>
      +65 6100 2400
    </li>
    <li>
      <svg viewBox="0 0 16 16" aria-hidden="true"><path d="M4 1h8v14H4zM5.5 2.5v9h5v-9z"/></svg>
      +65 9100 5521
    </li>
    <li>
      <svg viewBox="0 0 16 16" aria-hidden="true"><path d="M4 1h8v4H4zM1 6h14v6h-3v3H4v-3H1zM5.5 10v3.5h5V10z"/></svg>
      +65 6100 2411
    </li>
    <li>
      <svg viewBox="0 0 16 16" aria-hidden="true"><path d="M1 3h14v10H1zM2.5 4.5 8 9l5.5-4.5z"/></svg>
      ravin@kaviraco.com
    </li>
  </ul>

  <address class="address" style="font-style: normal;">
    18 Lantern Bay Rd<br>
    Singapore 100482
  </address>
</section>

</body>
</html>
```